Kaffeerösterei sucht Etiketten-Design
- schnelle Ausführung - mein Geschmack voll getroffen - unkompliziert und Kunden orientiert bei der Ausführung
Zielgruppe
Kaffeerösterei für die edelsten und teuersten Rohkaffees.
Meine Kunden sind Kaffee Geniesser.
Aufgabenstellung
Transparente Aufkleber für eine Schiefertafel im Format 22.5 cm x 15.5 cm.
Im Hand-Lettering Stil.
5 Schiefertafeln sind gewünscht.
Tafel 1
Kostenlos zur Degustation
Espresso
Café Crème 3.--
Americano 3.--
Filter Kaffee 3.--
Tafel 2
Kaffee & Milch
Cappuccino 4.--
Café Latte 4.--
Flat White 4.--
Latte Macchiato 4.--
Latte Macchiato mit Aroma 5.--
Kaffee & Hafermilch + 1.--
Tafel 3
Crepes
Pikant
- Pizza Crepes 7.--
- Flammkuchen Crepes 7.--
Süss
- Schoggi Crepes 6.--
- Apfelmus & Zimtzucker 6.--
Tafel 4
Kaffee & Schnaps
- Original Entlebucher Schwarzes 7.--
- Espresso Coretto 5.00
- Schwarzes mit Rahmhaube 8.--
Tafel 5
Schokolade & Milch
- heisse Schoggi 5.--
- heisse Schoggi mit Rahmhaube 6.--
- heisse Schoggi mit Espresso 6.--
- Schokolade & Hafermilch +1.--
Als Idee, was mir gefallen könnte:
https://www.bildsammlora.com/pin/507133820914462870/
https://de.grafivoro.com/vektorkunst/4180952-set-kaffeekarte-mit-tassen-kaffeegetranken-im-vintage-stil-stilisierte-zeichnung-mit-kreide-auf-tafel-schriftzug-know-your-coffee
https://www.fotelquin.de/stockfoto-heisser-kakao-bar-warm-hier-oben-hand-tafel-caf-schild-an-tafel-hintergrund-mit-farbe-kreide-schriftzug-werbung-fur-heisse-d-538172046.html

```html
<!DOCTYPE html>
<html lang="de">
<head>
<meta charset="utf-8">
<title>Kaffee &amp; Schnaps – Tafel</title>
<link rel="stylesheet" href="https://fonts.googleapis.com/css2?family=Amatic+SC:wght@700&display=swap">
<style>
  :root {
    --paper: #ffffff;
    --board: #1d1d1b;
    --chalk: #ffffff;
    --accent: #fdcd78;
    --price: #fdecd4;
  }
  html, body {
    margin: 0;
    padding: 0;
    width: 1200px;
    height: 879px;
    overflow: hidden;
    background: var(--paper);
  }
  .menu-board {
    display: block;
    width: 1200px;
    height: 879px;
  }
  .board-surface { fill: var(--board); }
  .chalk-frame {
    fill: none;
    stroke: var(--chalk);
    stroke-width: 4;
    stroke-linecap: round;
    stroke-linejoin: round;
  }
  .accent-stroke {
    fill: none;
    stroke: var(--accent);
    stroke-linecap: round;
  }
  .star-stroke {
    stroke: var(--chalk);
    stroke-width: 3.5;
    stroke-linecap: round;
  }
  .board-title {
    font-family: "Amatic SC", cursive;
    font-weight: 700;
    font-size: 122px;
    fill: var(--chalk);
  }
  .item-name {
    font-family: "Amatic SC", cursive;
    font-weight: 700;
    font-size: 66px;
    fill: var(--chalk);
    letter-spacing: 1px;
  }
  .item-price {
    font-family: "Amatic SC", cursive;
    font-weight: 700;
    font-size: 70px;
    fill: var(--price);
  }
  .drink-illustration { fill: #8a8a86; }
</style>
</head>
<body>
<svg class="menu-board" viewBox="0 0 1200 879" xmlns="http://www.w3.org/2000/svg">
  <rect class="board-surface" x="61" y="64" width="1076" height="741"/>

  <!-- chalk frame -->
  <g class="chalk-frame">
    <path d="M86 90 L398 86 M410 86 L422 86 M432 87 L436 87 M456 88 L466 89"/>
    <path d="M774 91 L780 91 M789 91 L808 91 M818 92 L1102 96"/>
    <path d="M86 90 L90 774 L1106 771 L1102 96"/>
    <circle cx="92" cy="97" r="7"/>
    <circle cx="1101" cy="102" r="8"/>
    <circle cx="96" cy="770" r="7"/>
    <circle cx="1102" cy="765" r="8"/>
    <path d="M1045 746 L1087 749 M1087 712 L1088 742"/>
  </g>
  <circle cx="1085" cy="694" r="2.5" fill="var(--chalk)"/>
  <circle cx="1031" cy="747" r="2.5" fill="var(--chalk)"/>

  <!-- title -->
  <text class="board-title" x="596" y="222" text-anchor="middle" textLength="686" lengthAdjust="spacingAndGlyphs">Kaffee &amp; Schnaps</text>

  <!-- title accents -->
  <g class="accent-stroke" stroke-width="6">
    <path d="M155 162 Q180 168 196 178"/>
    <path d="M132 187 Q165 190 188 193"/>
    <path d="M155 218 Q175 212 192 204"/>
    <path d="M1003 185 Q1030 180 1046 174"/>
    <path d="M1010 202 Q1040 201 1062 205"/>
    <path d="M1003 210 Q1020 222 1034 232"/>
  </g>
  <g class="star-stroke">
    <path d="M212 181 L212 210 M201 187 L223 204 M223 187 L201 204"/>
    <path d="M978 178 L978 216 M965 186 L991 208 M991 186 L965 208"/>
  </g>
  <path class="accent-stroke" stroke-width="8" d="M358 246 Q600 232 836 253"/>

  <!-- drink illustration -->
  <rect class="drink-illustration" x="141" y="356" width="199" height="351" rx="14" role="img" aria-label="Kreidezeichnung eines Glases mit heissem Kaffeegetränk und zwei Zimtstangen"/>

  <!-- menu items -->
  <g class="menu-items">
    <text class="item-name" x="850" y="379" text-anchor="end">Original Entlebucher</text>
    <text class="item-name" x="850" y="441" text-anchor="end">Schwarzes</text>
    <text class="item-price" x="885" y="441">7,–</text>

    <text class="item-name" x="850" y="528" text-anchor="end">Espresso Coretto</text>
    <text class="item-price" x="888" y="528">5,–</text>

    <text class="item-name" x="850" y="616" text-anchor="end">Schwarzes</text>
    <text class="item-name" x="850" y="678" text-anchor="end">mit Rahmhaube</text>
    <text class="item-price" x="888" y="678">8,–</text>
  </g>
</svg>
</body>
</html>
```